Dorian's Roam Almanac Mobile App

We need a sleek new design for our new mobile app we are launching in the South Pacific. This app will be released for both iPhone and Android. The app has already been developed and your new design will give it the finishing touch we need to release it to our audience. This will be the premiere tourism app for the South Pacific and will be advertised heavily in our successful print publications which are distributed internationally. We are looking for you to provide two designs (for two screens in our mobile app) for this competition. The selected winner will have the opportunity to design the remaining screens in our app and website as a separate contract.

Attached you will see a few of the screens that currently exist in our mobile app to give you a feel for the functionality. The two screens we want you to design for this competition are the main listing page and the category selection page. These two screens will be included in the uploaded files and will be clearly marked so you know what we are looking for.

Please feel free to reach out to us with any questions if you need any guidance in directing your designs. Show us something sleek, engaging, and ultimately something that will drive our users to want to engage with the businesses that are listed in the app.

Please see the uploaded files for a couple of our current designs, the two screens we want you to design for this competition, and a few samples of design ideas we like.

Best of Luck!

Target Market(s)

Travelers to the South Pacific

Industry/Entity Type

Travel Industry

Font styles to use
Serif
Sans Serif

Colors
0492cd
33a6d7
ec1f27
f04a50
85cae6
cee9f5
f59296
cedeed
fbd4d5

Requirements
Must have
• Clean, attractive design for the two screens mentioned in the brief.
Nice to have
• Icon sets, color guide, font selection
Should not have
• Project should not be too busy or incorporate too many different colors, styles, fonts, etc.

```html
<!DOCTYPE html>
<html lang="en">
<head>
<meta charset="UTF-8">
<title>Marlows – Listing</title>
<link href="https://fonts.googleapis.com/css2?family=Roboto:wght@400;500;700&display=swap" rel="stylesheet">
<style>
  :root {
    --hero-deep: #0a4fc4;
    --hero-light: #2f78e0;
    --ink: #222222;
    --text: #333333;
    --muted: #666666;
    --icon: #4a4a4a;
    --nav-icon: #a8a8a8;
    --line: #dcdcdc;
    --rating: #f26522;
    --accent: #ec1f27;
    --fab-top: #e0114f;
    --fab-bottom: #ef4a2a;
    --map-tone-a: #ebebe8;
    --map-tone-b: #e2e5e9;
    --white: #ffffff;
  }
  * { box-sizing: border-box; margin: 0; padding: 0; }
  html, body { width: 675px; height: 1200px; overflow: hidden; background: var(--white); }
  body { font-family: "Roboto", Arial, sans-serif; color: var(--text); position: relative; }

  .hero {
    position: absolute; left: 0; top: 0; width: 675px; height: 312px;
    background: linear-gradient(180deg, var(--hero-deep) 0%, var(--hero-light) 55%, #1f5fbf 100%);
  }
  .status-bar {
    position: absolute; top: 0; left: 0; width: 675px; height: 52px;
    color: var(--white); font-size: 20px; display: flex; align-items: center; padding: 0 12px;
  }
  .status-bar .carrier { display: flex; align-items: center; gap: 6px; }
  .status-bar .dots { letter-spacing: 1px; font-size: 14px; }
  .status-bar .time { position: absolute; left: 0; right: 0; text-align: center; font-weight: 500; pointer-events: none; }
  .status-bar .battery { margin-left: auto; display: flex; align-items: center; gap: 8px; }
  .hero-nav { position: absolute; top: 78px; left: 14px; right: 14px; display: flex; justify-content: space-between; }

  .title-card {
    position: absolute; left: 0; top: 312px; width: 675px; height: 101px;
    background: var(--white); box-shadow: 0 3px 6px rgba(0,0,0,0.15); z-index: 2;
  }
  .listing-name { position: absolute; left: 27px; top: 26px; font-size: 20px; font-weight: 700; color: var(--ink); }
  .rating-row { position: absolute; left: 27px; top: 59px; display: flex; align-items: center; gap: 8px; font-size: 15px; }
  .rating-score { color: var(--rating); }
  .rating-stars { display: flex; gap: 2px; }
  .review-count { color: var(--text); margin-left: 6px; }
  .favourite { position: absolute; left: 605px; top: 27px; }

  .actions { position: absolute; left: 0; top: 413px; width: 675px; height: 134px; display: flex; }
  .action { flex: 1; position: relative; border-right: 1px solid var(--line); }
  .action:last-child { border-right: none; }
  .action-circle {
    position: absolute; left: 50%; top: 22px; width: 61px; height: 61px; margin-left: -30px;
    border-radius: 50%; background: var(--white); box-shadow: 0 1px 5px rgba(0,0,0,0.2);
    display: flex; align-items: center; justify-content: center;
  }
  .action-label { position: absolute; left: 0; right: 0; top: 96px; text-align: center; font-size: 15px; color: var(--muted); }

  .map { position: absolute; left: 0; top: 547px; width: 675px; height: 194px;
    background: linear-gradient(135deg, var(--map-tone-a) 0%, var(--map-tone-b) 100%); }

  .info-row { position: absolute; left: 0; width: 675px; border-bottom: 1px solid var(--line); display: flex; align-items: center; }
  .info-row .info-icon { width: 92px; display: flex; justify-content: center; padding-right: 8px; }
  .info-row .info-text { font-size: 13.5px; color: var(--ink); }

  .btn { position: absolute; top: 998px; height: 57px; border-radius: 4px; font-size: 14.5px; display: flex; align-items: center; justify-content: center; }
  .btn-rate { left: 31px; width: 199px; background: var(--accent); color: var(--white); }
  .btn-reviews { left: 437px; width: 202px; border: 1px solid #c8c8c8; color: var(--muted); background: var(--white); }

  .tab-bar { position: absolute; left: 4px; right: 0; top: 1097px; height: 103px; border-top: 1px solid var(--line); }
  .tab { position: absolute; top: 30px; }
  .fab {
    position: absolute; left: 289px; top: 1080px; width: 108px; height: 108px; border-radius: 50%;
    background: linear-gradient(180deg, var(--fab-top), var(--fab-bottom));
    box-shadow: 0 6px 14px rgba(236,31,39,0.3);
    display: flex; align-items: center; justify-content: center;
  }
</style>
</head>
<body>
  <div class="hero" role="img" aria-label="Blue-tinted photo of a city skyline with domes and towers, birds in the sky"></div>

  <div class="status-bar">
    <div class="carrier"><span class="dots">●●●○○</span><span>NOVA</span>
      <svg width="20" height="15" viewBox="0 0 20 15"><path d="M10 14l3-3.5a4.5 4.5 0 0 0-6 0z M4.5 8.5a8 8 0 0 1 11 0l-1.6 1.8a5.6 5.6 0 0 0-7.8 0z M1.5 5a12.5 12.5 0 0 1 17 0l-1.6 1.8a10 10 0 0 0-13.8 0z" fill="#fff"/></svg>
    </div>
    <div class="time">4:21 PM</div>
    <div class="battery">
      <svg width="12" height="20" viewBox="0 0 12 20"><path d="M1 5l10 10-5 4V1l5 4L1 15" fill="none" stroke="#9fb6ee" stroke-width="1.6"/></svg>
      <span>22%</span>
      <svg width="40" height="18" viewBox="0 0 40 18"><rect x="1" y="1" width="34" height="16" rx="3" fill="none" stroke="#fff" stroke-width="1.5"/><rect x="3" y="3" width="7" height="12" rx="1" fill="#fff"/><rect x="36" y="6" width="3" height="6" rx="1" fill="#fff"/></svg>
    </div>
  </div>

  <nav class="hero-nav">
    <svg width="36" height="30" viewBox="0 0 36 30" aria-label="Back"><path d="M34 15H4 M15 3L3 15l12 12" fill="none" stroke="#fff" stroke-width="3"/></svg>
    <svg width="36" height="30" viewBox="0 0 36 30" aria-label="Menu"><path d="M1 4h34 M1 15h34 M1 26h34" stroke="#fff" stroke-width="3"/></svg>
  </nav>

  <section class="title-card">
    <h1 class="listing-name">Marlows</h1>
    <div class="rating-row">
      <span class="rating-score">4.0</span>
      <span class="rating-stars">
        <svg width="84" height="16" viewBox="0 0 84 16" fill="#f26522">
          <path id="st" d="M8 0.5l2.2 5 5.4.5-4.1 3.6 1.2 5.3L8 12.1 3.3 14.9l1.2-5.3L.4 6l5.4-.5z"/>
          <use href="#st" x="17"/><use href="#st" x="34"/><use href="#st" x="51"/><use href="#st" x="68"/>
        </svg>
      </span>
      <span class="review-count">10 Reviews</span>
    </div>
    <svg class="favourite" width="42" height="40" viewBox="0 0 42 40" aria-label="Add to favourites"><path d="M21 2l5.6 12.2 13.3 1.4-10 9 2.9 13.1L21 31l-11.8 6.7 2.9-13.1-10-9 13.3-1.4z" fill="none" stroke="#444" stroke-width="1.6" stroke-linejoin="round"/></svg>
  </section>

  <section class="actions">
    <div class="action">
      <div class="action-circle"><svg width="30" height="26" viewBox="0 0 30 26"><path d="M18 2l10 9-10 9v-5c-7 0-12 2-16 8 1-8 6-14 16-15z" fill="none" stroke="#444" stroke-width="1.6" stroke-linejoin="round"/></svg></div>
      <div class="action-label">Directions</div>
    </div>
    <div class="action">
      <div class="action-circle" style="top:26px"><svg width="28" height="28" viewBox="0 0 24 24"><path d="M6.6 10.8a15.5 15.5 0 0 0 6.6 6.6l2.2-2.2c.3-.3.7-.4 1-.2 1.1.4 2.3.6 3.6.6.6 0 1 .4 1 1V20c0 .6-.4 1-1 1C10.6 21 3 13.4 3 4c0-.6.4-1 1-1h3.5c.6 0 1 .4 1 1 0 1.3.2 2.5.6 3.6.1.3 0 .7-.2 1z" fill="#444"/></svg></div>
      <div class="action-label" style="top:100px">Call</div>
    </div>
    <div class="action">
      <div class="action-circle" style="top:24px"><svg width="30" height="30" viewBox="0 0 30 30"><circle cx="15" cy="15" r="13" fill="#444"/><path d="M7 8c3 0 4 2 6 2s2 3 0 4-1 4-3 5-1-3-3-4-2-5 0-7zM18 4c2 1 1 3 3 4s4 1 5 4c-2 0-3 2-2 4s-1 5-3 6c0-3-2-4-3-6s1-4-1-5 0-5 1-7z" fill="#fff"/></svg></div>
      <div class="action-label" style="top:98px">Website</div>
    </div>
  </section>

  <div class="map" role="img" aria-label="Street map showing the area around the listing"></div>

  <div class="info-row" style="top:741px;height:78px">
    <div class="info-icon"><svg width="30" height="40" viewBox="0 0 30 40"><path d="M15 1C7 1 1 7 1 15c0 10 14 24 14 24s14-14 14-24C29 7 23 1 15 1zm0 19a5 5 0 1 1 0-10 5 5 0 0 1 0 10z" fill="#4a4a4a"/></svg></div>
    <div class="info-text">Lorem Ipsum is simply dummy text of the printing and typesetting industry.</div>
  </div>
  <div class="info-row" style="top:819px;height:77px">
    <div class="info-icon"><svg width="34" height="34" viewBox="0 0 24 24"><path d="M6.6 10.8a15.5 15.5 0 0 0 6.6 6.6l2.2-2.2c.3-.3.7-.4 1-.2 1.1.4 2.3.6 3.6.6.6 0 1 .4 1 1V20c0 .6-.4 1-1 1C10.6 21 3 13.4 3 4c0-.6.4-1 1-1h3.5c.6 0 1 .4 1 1 0 1.3.2 2.5.6 3.6.1.3 0 .7-.2 1z" fill="#4a4a4a"/></svg></div>
    <div class="info-text">000 0000 0000</div>
  </div>
  <div class="info-row" style="top:896px;height:71px">
    <div class="info-icon"><svg width="30" height="30" viewBox="0 0 30 30"><circle cx="15" cy="15" r="14" fill="#4a4a4a"/><path d="M6 8c3 0 4 2 6 2s2 3 0 4-1 4-3 5-1-3-3-4-2-5 0-7zM18 3c2 1 1 3 3 4s4 1 6 4c-2 0-3 2-2 4s-1 6-3 7c0-3-2-4-3-6s1-4-1-5 0-6 0-8z" fill="#fff"/></svg></div>
    <div class="info-text">https://www.marlows.com</div>
  </div>

  <div class="btn btn-rate">Rate It!</div>
  <div class="btn btn-reviews">Read Reviews</div>

  <nav class="tab-bar">
    <svg class="tab" style="left:67px" width="38" height="38" viewBox="0 0 38 38"><path d="M3 3h32v25H10l-7 7z" fill="none" stroke="#a8a8a8" stroke-width="3" stroke-linejoin="round"/><path d="M10 11h18M10 16h18M10 21h12" stroke="#a8a8a8" stroke-width="3"/></svg>
    <svg class="tab" style="left:185px;top:36px" width="44" height="28" viewBox="0 0 44 28"><circle cx="13" cy="7" r="5.5" fill="none" stroke="#a8a8a8" stroke-width="2.5"/><circle cx="31" cy="7" r="5.5" fill="none" stroke="#a8a8a8" stroke-width="2.5"/><path d="M2 26v-3c0-4 5-7 11-7s11 3 11 7v3zM24 16.5c2-.4 4-.5 7-.5 6 0 11 3 11 7v3H24" fill="none" stroke="#a8a8a8" stroke-width="2.5"/></svg>
    <svg class="tab" style="left:449px;top:34px" width="38" height="30" viewBox="0 0 38 30"><circle cx="3" cy="3" r="2.5" fill="#a8a8a8"/><circle cx="3" cy="15" r="2.5" fill="#a8a8a8"/><circle cx="3" cy="27" r="2.5" fill="#a8a8a8"/><path d="M11 3h26M11 15h26M11 27h26" stroke="#a8a8a8" stroke-width="3"/></svg>
    <svg class="tab" style="left:576px;top:31px" width="32" height="34" viewBox="0 0 32 34"><circle cx="16" cy="9" r="7" fill="none" stroke="#a8a8a8" stroke-width="3"/><path d="M2 32v-3c0-5 7-8 14-8s14 3 14 8v3z" fill="none" stroke="#a8a8a8" stroke-width="3"/></svg>
  </nav>
  <div class="fab" aria-label="Add"><svg width="30" height="30" viewBox="0 0 30 30"><path d="M15 2v26M2 15h26" stroke="#fff" stroke-width="3.5"/></svg></div>
</body>
</html>
```